Business Card For Birchfield Property Partners Corp.
Birchfield Property Partners Corp.
Business Card For Birchfield Property Partners Corp. - Real Estate
Creative Brief
Modern
Warren T. Caldwell
Owner
418 Larkspur Avenue, Huntington NY 11749
warrencaldwell@brightmailer.net
www.birchfieldpropertypartners.com
Catch Phrases: Complete Home Service Solution Take your first step toward financial freedom today
Maybe Some other design symbolizing fast cash for homes with a catch phrase: Birchfield Property Partners will purchase any home in any condition

```html
<!DOCTYPE html>
<html lang="en">
<head>
<meta charset="utf-8">
<title>Birchfield Property Partners Corp. – Business Card</title>
<link rel="stylesheet" href="https://fonts.googleapis.com/css2?family=Open+Sans:wght@400;600;700&display=swap">
<style>
  :root {
    --page-bg: #e9e7e3;
    --card-bg: #ffffff;
    --brand-blue: #2f74b5;
    --brand-green: #7fb241;
    --name-blue: #3d6283;
    --text-grey: #4a4a4a;
    --muted-grey: #7a7a7a;
    --icon-dark: #3b3b3b;
  }
  * { margin: 0; padding: 0; box-sizing: border-box; }
  html, body {
    width: 1200px; height: 902px; overflow: hidden;
    background: var(--page-bg);
    font-family: "Open Sans", Arial, sans-serif;
  }
  .business-card {
    position: absolute;
    left: 100px; top: 165px;
    width: 1000px; height: 572px;
    background: var(--card-bg);
    box-shadow: 0 6px 24px rgba(0,0,0,0.18);
  }
  .brand-mark-area {
    position: absolute;
    left: 70px; top: 120px;
    width: 340px; height: 340px;
    border-radius: 50%;
    background: radial-gradient(circle at 40% 40%, #cfe4b4 0%, #a9cd7c 100%);
  }
  .card-details {
    position: absolute;
    right: 56px; top: 52px;
    text-align: right;
  }
  .company-name {
    color: var(--brand-blue);
    font-weight: 700;
    font-size: 40px;
    line-height: 1.08;
    letter-spacing: -0.5px;
  }
  .person-name {
    margin-top: 22px;
    color: var(--name-blue);
    font-weight: 700;
    font-size: 26px;
  }
  .person-title {
    color: var(--muted-grey);
    font-size: 19px;
    margin-right: 34px;
  }
  .contact-list {
    list-style: none;
    margin-top: 26px;
    color: var(--text-grey);
    font-size: 17px;
    line-height: 1.45;
  }
  .contact-list li {
    display: flex; justify-content: flex-end; align-items: center; gap: 10px;
  }
  .contact-list .no-icon { margin-right: 30px; }
  .contact-list .gap-before { margin-top: 12px; }
  .contact-icon { width: 20px; height: 20px; flex: none; }
</style>
</head>
<body>
  <div class="business-card">
    <div class="brand-mark-area" aria-hidden="true"></div>
    <div class="card-details">
      <div class="company-name">Birchfield Property<br>Partners</div>
      <div class="person-name">Warren T. Caldwell</div>
      <div class="person-title">Owner</div>
      <ul class="contact-list">
        <li>418 Larkspur Avenue, Huntington
          <svg class="contact-icon" viewBox="0 0 20 20" aria-hidden="true"><circle cx="10" cy="10" r="10" fill="var(--icon-dark)"/><path d="M10 4.5a3.3 3.3 0 0 0-3.3 3.3c0 2.6 3.3 6.9 3.3 6.9s3.3-4.3 3.3-6.9A3.3 3.3 0 0 0 10 4.5zm0 4.6a1.3 1.3 0 1 1 0-2.6 1.3 1.3 0 0 1 0 2.6z" fill="#fff"/></svg></li>
        <li class="no-icon">NY 11749</li>
        <li>555-318-4400
          <svg class="contact-icon" viewBox="0 0 20 20" aria-hidden="true"><circle cx="10" cy="10" r="10" fill="var(--icon-dark)"/><path d="M7 5l2 2.6-1.1 1.2a6 6 0 0 0 3.3 3.3l1.2-1.1L15 13l-1 1.6c-4.2 0-8.6-4.4-8.6-8.6z" fill="#fff"/></svg></li>
        <li>555-318-4427
          <svg class="contact-icon" viewBox="0 0 20 20" aria-hidden="true"><circle cx="10" cy="10" r="10" fill="var(--icon-dark)"/><rect x="7" y="4.5" width="6" height="11" rx="1.2" fill="#fff"/><rect x="8" y="6" width="4" height="6.5" fill="var(--icon-dark)"/></svg></li>
        <li>555-318-4460
          <svg class="contact-icon" viewBox="0 0 20 20" aria-hidden="true"><circle cx="10" cy="10" r="10" fill="var(--icon-dark)"/><rect x="5.5" y="8" width="9" height="5" rx="1" fill="#fff"/><rect x="7" y="5" width="6" height="3" fill="#fff"/><rect x="7" y="11.5" width="6" height="3.5" fill="#fff" stroke="var(--icon-dark)" stroke-width="0.8"/></svg></li>
        <li class="gap-before">warrencaldwell@brightmailer.net
          <svg class="contact-icon" viewBox="0 0 20 20" aria-hidden="true"><circle cx="10" cy="10" r="10" fill="var(--icon-dark)"/><rect x="5" y="6.5" width="10" height="7" rx="0.8" fill="#fff"/><path d="M5.3 7l4.7 3.6L14.7 7" fill="none" stroke="var(--icon-dark)" stroke-width="1"/></svg></li>
        <li>www.birchfieldpropertypartners.com
          <svg class="contact-icon" viewBox="0 0 20 20" aria-hidden="true"><circle cx="10" cy="10" r="10" fill="var(--icon-dark)"/><circle cx="10" cy="10" r="5" fill="none" stroke="#fff" stroke-width="1.1"/><ellipse cx="10" cy="10" rx="2.2" ry="5" fill="none" stroke="#fff" stroke-width="1"/><path d="M5 10h10" stroke="#fff" stroke-width="1"/></svg></li>
      </ul>
    </div>
  </div>
</body>
</html>
```